Sunscreen Package Design Modern SPF 50

Update current package design to a more modern design target women 16-40 Do not make it playful. Mirada Bay is home to movie stars and high income business people PalmSprings is one of the most desired vacation areas in the world. The sun shines 350 days a year. World class Tennis and Golf tournaments are held every year with the worlds top players attending these tournaments

Target Market(s)

Women

Industry/Entity Type

Skin Protection

Font styles to use
Sans Serif

Requirements
Must have
• The words Mirada Bay and VELORIMA

```html
<!DOCTYPE html>
<html lang="en">
<head>
<meta charset="utf-8">
<title>Mirada Bay VELORIMA – Sun Care Labels</title>
<link rel="stylesheet" href="https://fonts.googleapis.com/css2?family=Montserrat:wght@400;500;600&display=swap">
<style>
  :root {
    --bg: #dcdcdc;
    --label: #efebe4;
    --ink: #3c3d3f;
    --gold: #b79168;
    --gold-dark: #8e6a45;
    --peach-light: #fbbd9a;
    --peach-dark: #a9755a;
    --aqua-light: #a6dfec;
    --aqua-dark: #5f98a6;
    --white: #ffffff;
  }
  * { margin: 0; padding: 0; box-sizing: border-box; }
  html, body { width: 1200px; height: 1200px; overflow: hidden; background: var(--bg); }
  .canvas { position: relative; width: 1200px; height: 1200px; background: var(--bg); }

  .label {
    position: absolute; top: 230px; width: 300px; height: 627px;
    background: var(--label); overflow: hidden;
    box-shadow: 0 14px 30px rgba(0,0,0,0.12);
  }
  .label--sunscreen { left: 178px; }
  .label--aftersun { left: 745px; }

  .label__wave { position: absolute; inset: 0; width: 300px; height: 627px; }

  .brand { position: absolute; left: 0; right: 0; text-align: center; color: var(--ink);
    font-family: "Montserrat", sans-serif; font-weight: 500; line-height: 1; }
  .brand--first { top: 255px; font-size: 50px; letter-spacing: 1px; }
  .brand--second { top: 318px; font-size: 40px; letter-spacing: 4px; }

  .maker { position: absolute; left: 0; right: 0; top: 370px; text-align: center;
    font-family: "Montserrat", sans-serif; font-weight: 500; font-size: 13px;
    letter-spacing: 6px; color: var(--gold); }
  .maker sup { font-size: 6px; letter-spacing: 0; }

  .rule { position: absolute; left: 125px; top: 402px; width: 50px; height: 1px; background: var(--gold); }

  .product { position: absolute; left: 0; right: 0; top: 417px; text-align: center;
    font-family: "Montserrat", sans-serif; font-weight: 500; font-size: 11px;
    letter-spacing: 4px; color: var(--ink); }

  .spf {
    position: absolute; left: 122px; top: 453px; width: 56px; height: 56px; border-radius: 50%;
    background: var(--label); border: 2px solid var(--gold);
    box-shadow: 0 0 0 2px var(--label), 0 0 0 3px rgba(183,145,104,0.5);
    display: flex; flex-direction: column; align-items: center; justify-content: center;
    font-family: "Montserrat", sans-serif; color: var(--gold-dark); line-height: 0.95;
  }
  .spf__word { font-size: 12px; font-weight: 400; }
  .spf__value { font-size: 19px; font-weight: 500; }

  .copy { position: absolute; left: 20px; right: 20px; text-align: center;
    font-family: "Montserrat", sans-serif; color: var(--white); }
  .copy--headline { top: 520px; font-size: 8.5px; font-weight: 600; letter-spacing: 1px; line-height: 1.25; }
  .copy--sub { top: 556px; font-size: 8px; font-weight: 600; letter-spacing: 0.3px; }
  .copy--fine { top: 569px; font-size: 5.5px; font-weight: 500; color: #4a3a33; line-height: 1.3; }
  .label--aftersun .copy--fine { color: #2f4a52; }
  .copy--size { top: 593px; font-size: 6.5px; font-weight: 400; opacity: 0.9; }
</style>
</head>
<body>
<div class="canvas">

  <section class="label label--sunscreen">
    <svg class="label__wave" viewBox="0 0 300 627" aria-hidden="true">
      <defs>
        <linearGradient id="peach" x1="0" y1="0" x2="1" y2="0">
          <stop offset="0" stop-color="#fbbd9a"/>
          <stop offset="0.5" stop-color="#e9a582"/>
          <stop offset="1" stop-color="#a9755a"/>
        </linearGradient>
      </defs>
      <path d="M0,585 C20,520 90,488 170,465 C230,446 285,420 300,370 L300,627 L0,627 Z" fill="url(#peach)"/>
      <path d="M0,585 C20,520 90,488 170,465 C230,446 285,420 300,370" fill="none" stroke="#b79168" stroke-width="2.5"/>
    </svg>
    <div class="brand brand--first">MIRADA</div>
    <div class="brand brand--second">BAY</div>
    <div class="maker">VELORIMA<sup>®</sup></div>
    <div class="rule"></div>
    <div class="product">SUNSCREEN</div>
    <div class="spf"><span class="spf__word">SPF</span><span class="spf__value">30</span></div>
    <p class="copy copy--headline">UVA + UVB<br>PROTECTION</p>
    <p class="copy copy--sub">BROAD SPECTRUM</p>
    <p class="copy copy--fine">WATER RESISTANT (80 MINUTES)</p>
    <p class="copy copy--size">3 FL OZ / 88ML</p>
  </section>

  <section class="label label--aftersun">
    <svg class="label__wave" viewBox="0 0 300 627" aria-hidden="true">
      <defs>
        <linearGradient id="aqua" x1="0" y1="0" x2="1" y2="0">
          <stop offset="0" stop-color="#a6dfec"/>
          <stop offset="0.5" stop-color="#86c2cf"/>
          <stop offset="1" stop-color="#5f98a6"/>
        </linearGradient>
      </defs>
      <path d="M0,585 C20,520 90,488 170,465 C230,446 285,420 300,370 L300,627 L0,627 Z" fill="url(#aqua)"/>
      <path d="M0,585 C20,520 90,488 170,465 C230,446 285,420 300,370" fill="none" stroke="#b79168" stroke-width="2.5"/>
    </svg>
    <div class="brand brand--first">MIRADA</div>
    <div class="brand brand--second">BAY</div>
    <div class="maker">VELORIMA<sup>®</sup></div>
    <div class="rule"></div>
    <div class="product">AFTERSUN</div>
    <div class="spf"><span class="spf__word">SPF</span><span class="spf__value">30</span></div>
    <p class="copy copy--headline">HYDRATE YOUR SKIN WITH<br>THESE ESSENTIAL<br>INGREDIENTS</p>
    <p class="copy copy--fine">HYALURONATE ACID CUCUMBER<br>ALOE JOJOBA SUNFLOWER</p>
    <p class="copy copy--size">3 FL OZ / 88ML</p>
  </section>

</div>
</body>
</html>
```